Business Card for Luxury Hospitality Industry Career Seeker

Need something Simple, Punctual, and Elegant.

Project goal is to update phone number, layout, and wording

I look forward to working with you to create a business card I can give to managers and employers in the Luxury Hospitality industry. I want to advance a career in this industry handing out cards to managers and directors on my way up.
Updates

Updated graphics preferences in brief - would like my name flanked by small Lion, Compass, & Rope and have the Halworth 5 Star logo on the back Added Saturday, January 14, 2017

Updated Brief:-Some wording has been removed-Card Front should be more simple and tidy now-Card Back word choice & flow is improved Added Sunday, January 15, 2017

Target Market(s)

Luxury Hospitality Industry Employers and Managers

Industry/Entity Type

Hospitality

Contact Information for Business Card

(Card Front)
Corbin T. Pellman (flanked by small Lion, Compass & Rope graphic)
Luxury Hospitality
555-317-8846
ridgefellow@mailvessel.example
netroster.example/in/corbin-pellman-vet-civ
My Experience = Our Success

(Card Back)
Graphic of: Halworth 5 Star logo and maybe QTR 5 Diamond Logo too
8 years military supply, logistics, & administrative experience
2 years intensive recruiting, marketing, and sales expertise
Adept problem solving, planning and management skills
5 Star, 5 Daimond, Luxury Hotels & Hospitality Rooms & Revenue

Requirements
Must have
• Name
• Phone Number
• Email Address
• Net Roster Address
• Slogan (My Experience = Our Success)
• Graphic on back: Halworth 5 Star logo
• Qualification Remarks
• Catchy logo
Nice to have
• Background that makes a viewer think Luxury Hospitality Experience and/or World Experience
• Color combinations I've seen & liked are black & yellow, black & white, and blue & white

```html
<!DOCTYPE html>
<html lang="en">
<head>
<meta charset="utf-8">
<title>Corbin T. Pellman – Business Card</title>
<link rel="stylesheet" href="https://fonts.googleapis.com/css2?family=Cinzel:wght@600;700&family=Montserrat:wght@400;500;600&display=swap">
<style>
  :root {
    --stage: #1c1c1e;
    --card-black: #050505;
    --accent-yellow: #f2e51b;
    --paper-white: #ffffff;
    --text-white: #f4f4f4;
    --gold: #b99a5c;
    --badge-blue: #2456a8;
    --emblem-grey: #1b1b1b;
  }
  * { box-sizing: border-box; margin: 0; padding: 0; }
  html, body { width: 1200px; height: 900px; overflow: hidden; background: var(--stage); }
  .canvas { position: relative; width: 1200px; height: 900px; }

  .card {
    position: absolute; left: 250px; width: 700px; height: 400px;
    background: var(--card-black); border-radius: 22px; overflow: hidden;
    font-family: "Montserrat", sans-serif; color: var(--text-white);
    box-shadow: 0 10px 30px rgba(0,0,0,.5);
  }
  .card-back { top: 30px; }
  .card-front { top: 470px; }
  .swoosh { position: absolute; inset: 0; width: 100%; height: 100%; }

  /* back */
  .emblem-watermark {
    position: absolute; left: 250px; top: 30px; width: 180px; height: 180px;
    border-radius: 50%; background: radial-gradient(circle, #222 0%, var(--emblem-grey) 60%, transparent 72%);
  }
  .rating-mark {
    position: absolute; left: 52px; top: 96px; display: flex; align-items: center; gap: 10px;
    font-family: "Cinzel", serif; font-weight: 700; font-size: 26px; color: var(--gold);
  }
  .rating-mark .dot { width: 18px; height: 18px; border-radius: 50%; background: var(--gold); }
  .award-mark {
    position: absolute; right: 54px; top: 30px; display: flex; align-items: center; gap: 10px;
    font-family: "Montserrat", sans-serif; font-weight: 600; font-size: 22px; color: var(--badge-blue);
  }
  .award-mark .badge { width: 56px; height: 56px; border-radius: 50%; background: var(--badge-blue); }
  .qualifications {
    position: absolute; left: 34px; top: 188px; list-style: none;
    font-size: 15.5px; line-height: 24px;
  }
  .qualifications li::before {
    content: ""; display: inline-block; width: 7px; height: 7px; border-radius: 50%;
    background: var(--accent-yellow); margin-right: 8px; vertical-align: middle;
  }

  /* front */
  .name-row { position: absolute; left: 60px; top: 92px; display: flex; align-items: center; gap: 22px; }
  .name {
    font-family: "Cinzel", serif; font-weight: 700; font-size: 33px; letter-spacing: 2px;
    color: var(--text-white); text-transform: uppercase;
  }
  .name-bar { position: absolute; left: 40px; top: 148px; width: 8px; height: 22px; background: var(--accent-yellow); }
  .emblem-small {
    width: 78px; height: 78px; border-radius: 50%;
    background: radial-gradient(circle, #e8e8e8 0%, #9a9a9a 70%, transparent 72%);
  }
  .role { position: absolute; left: 66px; top: 142px; color: var(--accent-yellow); font-weight: 500; font-size: 18px; line-height: 26px; }
  .contacts { position: absolute; left: 66px; top: 206px; list-style: none; font-size: 17px; line-height: 28px; }
  .contacts li { display: flex; align-items: center; gap: 12px; }
  .contacts svg { width: 16px; height: 16px; flex: none; }
  .slogan {
    position: absolute; left: 66px; top: 294px;
    font-family: "Cinzel", serif; font-weight: 600; font-size: 18px; letter-spacing: 1.5px;
    color: var(--accent-yellow); text-transform: uppercase;
  }
</style>
</head>
<body>
<main class="canvas">

  <section class="card card-back">
    <div class="emblem-watermark" role="img" aria-label="Faint Lion, Compass & Rope emblem"></div>
    <div class="award-mark"><span class="badge"></span>QTR</div>
    <div class="rating-mark"><span class="dot"></span>Halworth</div>
    <svg class="swoosh" viewBox="0 0 700 400" preserveAspectRatio="none" aria-hidden="true">
      <path d="M320 350 Q540 320 700 252 L700 240 Q540 308 320 350 Z" fill="var(--accent-yellow)"/>
      <path d="M0 400 L0 352 Q440 380 700 270 L700 400 Z" fill="var(--paper-white)"/>
    </svg>
    <ul class="qualifications">
      <li>8 years military supply, logistics, &amp; administrative experience</li>
      <li>2 years intensive recruiting, marketing, and sales expertise</li>
      <li>Adept problem solving, planning and management skills</li>
      <li>5 Star, 5 Daimond, Luxury Hotels &amp; Hospitality Rooms &amp; Revenue</li>
    </ul>
  </section>

  <section class="card card-front">
    <svg class="swoosh" viewBox="0 0 700 400" preserveAspectRatio="none" aria-hidden="true">
      <path d="M0 400 L0 370 Q440 350 680 250 Q460 370 120 400 Z" fill="var(--accent-yellow)"/>
      <path d="M60 400 Q480 370 700 236 L700 400 Z" fill="var(--paper-white)"/>
    </svg>
    <div class="name-bar"></div>
    <div class="name-row">
      <h1 class="name">Corbin T. Pellman</h1>
      <div class="emblem-small" role="img" aria-label="Small Lion, Compass & Rope emblem"></div>
    </div>
    <p class="role">Reservations Agent<br>Halworth 5 Star Luxury Hotel</p>
    <ul class="contacts">
      <li><svg viewBox="0 0 16 16"><path d="M3 1 L6 1 L7 5 L5 6.5 Q6.5 9.5 9.5 11 L11 9 L15 10 L15 13 Q15 15 13 15 Q2 14 1 3 Q1 1 3 1 Z" fill="var(--accent-yellow)"/></svg>555-317-8846</li>
      <li><svg viewBox="0 0 16 16"><rect x="1" y="3" width="14" height="10" rx="1" fill="none" stroke="var(--accent-yellow)" stroke-width="1.6"/><path d="M1.5 4 L8 9 L14.5 4" fill="none" stroke="var(--accent-yellow)" stroke-width="1.6"/></svg>ridgefellow@mailvessel.example</li>
      <li><svg viewBox="0 0 16 16"><circle cx="8" cy="8" r="6" fill="var(--accent-yellow)"/></svg>netroster.example/in/corbin-pellman-vet-civ</li>
    </ul>
    <p class="slogan">My Experience = Our Success</p>
  </section>

</main>
</body>
</html>
```